Harbourline Works Group Business Card Redesign

Logo has already been developed. The current business card is one sided. We'd like our mission on the back and more creativity so it pops. We may also like a tagline on the back
One call...all the service, all the savings. Examples are attached from our printer but we don't like them. The front is how we have our existing cards but the back is new. We are open to all ideas. We do like our colors/ brand of purple, black, white...

```html
<!DOCTYPE html>
<html lang="en">
<head>
<meta charset="utf-8">
<title>Harbourline Works Group Business Cards</title>
<link rel="stylesheet" href="https://fonts.googleapis.com/css2?family=Roboto:wght@400;700;900&family=Crimson+Text:wght@400;700&display=swap">
<style>
  :root {
    --brand-purple: #6a2c91;
    --ink: #262626;
    --card-white: #fbfbf9;
    --backdrop: #ecebe8;
  }
  * { box-sizing: border-box; margin: 0; padding: 0; }
  html, body { width: 1200px; height: 800px; overflow: hidden; }
  body {
    background: var(--backdrop);
    display: flex;
    align-items: center;
    justify-content: center;
    gap: 40px;
  }
  .card {
    position: relative;
    width: 540px;
    height: 309px;
    background: var(--card-white);
    box-shadow: 0 2px 6px rgba(0,0,0,0.12);
  }

  /* Brand lockup: name plus a plain circle */
  .brand {
    position: absolute;
    display: flex;
    align-items: center;
    gap: 12px;
  }
  .brand-dot {
    width: 46px; height: 46px;
    border-radius: 50%;
    background: var(--brand-purple);
    flex: none;
  }
  .brand-name {
    font-family: "Roboto", sans-serif;
    font-weight: 700;
    font-size: 19px;
    line-height: 1.05;
    color: var(--ink);
  }

  /* Back: mission side */
  .card-back .brand { left: 120px; top: 36px; }
  .tagline-band {
    position: absolute;
    left: 70px; right: 70px; top: 112px;
    height: 78px;
    border-radius: 39px;
    background: var(--brand-purple);
    color: #fff;
    font-family: "Roboto", sans-serif;
    font-weight: 700;
    text-align: center;
    display: flex;
    flex-direction: column;
    justify-content: center;
    line-height: 1.15;
  }
  .tagline-lead { font-size: 22px; }
  .tagline-main { font-size: 23px; }
  .mission {
    position: absolute;
    left: 30px; right: 30px; top: 200px;
    text-align: center;
    font-family: "Roboto", sans-serif;
    color: var(--brand-purple);
  }
  .mission-title {
    font-size: 13px;
    text-decoration: underline;
    margin-bottom: 4px;
  }
  .mission-text { font-size: 14px; line-height: 1.3; }

  /* Front: contact side */
  .card-front .brand { left: 150px; top: 34px; }
  .person {
    position: absolute;
    left: 0; right: 0; top: 118px;
    text-align: center;
    font-family: "Crimson Text", serif;
    color: var(--ink);
    padding-right: 60px;
  }
  .person-name { font-size: 24px; font-weight: 700; line-height: 1.1; }
  .person-role { font-size: 16px; }
  .phones {
    position: absolute;
    right: 26px; top: 96px;
    text-align: right;
    font-family: "Crimson Text", serif;
    font-size: 16px;
    line-height: 1.35;
    color: var(--ink);
  }
  .address {
    position: absolute;
    left: 26px; bottom: 22px;
    font-family: "Crimson Text", serif;
    font-size: 16px;
    line-height: 1.35;
    color: var(--ink);
  }
  .email {
    position: absolute;
    left: 205px; bottom: 22px;
    font-family: "Crimson Text", serif;
    font-size: 15px;
    color: var(--ink);
  }
</style>
</head>
<body>

  <section class="card card-back" aria-label="Card back">
    <div class="brand">
      <span class="brand-dot"></span>
      <span class="brand-name">Harbourline<br>Works<br>Group</span>
    </div>
    <div class="tagline-band">
      <span class="tagline-lead">One Call</span>
      <span class="tagline-main">All the Service - All the Savings</span>
    </div>
    <div class="mission">
      <p class="mission-title">Our Mission</p>
      <p class="mission-text">To ensure the injured worker returns to function and work, faster, better, stronger while creating longterm client loyalty through service and value we provide.</p>
    </div>
  </section>

  <section class="card card-front" aria-label="Card front">
    <div class="brand">
      <span class="brand-dot"></span>
      <span class="brand-name">Harbourline<br>Works<br>Group</span>
    </div>
    <div class="phones">
      <p>Main: (555) 310-4720</p>
      <p>Fax: (555) 310-4721</p>
      <p>Cell: (555) 864-2093</p>
      <p>www.HarbourlineWorksGroup.com</p>
    </div>
    <div class="person">
      <p class="person-name">Dale Whitford</p>
      <p class="person-role">Business Development Manager</p>
    </div>
    <div class="address">
      <p>418 W. Marlow Avenue</p>
      <p>Suite 200</p>
      <p>Fairhaven, AZ 85099</p>
    </div>
    <p class="email">e-mail: dwhitford@HarbourlineWorksGroup.com</p>
  </section>

</body>
</html>
```